PTA Sign 24”x60”

We need a design for our PTA sign (24”x60”) that is going next to a table (attached is an image of the sign)

I'd like the color scheme to royal blue in the website below and I've attached a few of our school logos.

It should have the colors and simple PTA logo of this tablecloth https://stores.brimlyshop.com/listings.lasso?c_id=Tablecloths&-session=KI_Clients:4QF2870D551ab7E19RwPLN3A826C

The most important thing is the words pop and is easy to read from far away.

Larkfield PTA

What do we do?
Help at school events
Support our school and students
Organize fundraising events
Have fun together!

Questions? Email PTALarkfield@quellmail.com

Get text updates - Text @larkfieldpta to the number 47326

Parents of Elementary School Students

Education

Sans Serif

• Clear words that pop- easy to read

```html
<!DOCTYPE html>
<html lang="en">
<head>
<meta charset="utf-8">
<title>Larkfield PTA Sign</title>
<link rel="stylesheet" href="https://fonts.googleapis.com/css2?family=Archivo:wght@300;400;700;800;900&display=swap">
<style>
  :root {
    --navy: #262a69;
    --red: #e3252b;
    --white: #ffffff;
    --backdrop: #e9e9ea;
    --ring: #d6d6d8;
    --mascot: #4a4f8a;
  }
  html, body { margin: 0; padding: 0; overflow: hidden; }
  body {
    width: 1200px; height: 1200px;
    background: var(--backdrop);
    font-family: "Archivo", Arial, sans-serif;
    position: relative;
  }
  .sign {
    position: absolute; left: 380px; top: 50px;
    width: 440px; height: 1100px;
    background: var(--navy); overflow: hidden; color: var(--white);
  }
  .sign-footer-bg { position: absolute; left: 0; top: 0; width: 440px; height: 1100px; }
  .title { position: absolute; left: 34px; top: 40px; margin: 0; font-weight: 900; line-height: 0.92; width: 380px; }
  .title .name { display: block; font-size: 54px; letter-spacing: -0.5px; white-space: nowrap; }
  .title .org { display: block; font-size: 118px; letter-spacing: -2px; }
  .rule { position: absolute; left: 37px; top: 247px; width: 367px; height: 3px; background: var(--red); }
  .question {
    position: absolute; left: 37px; top: 270px; margin: 0;
    font-size: 66px; font-weight: 300; line-height: 0.92; letter-spacing: -1px;
  }
  .question .accent { color: var(--red); font-weight: 800; }
  .activities { position: absolute; left: 37px; top: 435px; margin: 0; padding: 0; list-style: none; width: 330px; }
  .activities li {
    position: relative; padding-left: 26px; margin-bottom: 25px;
    font-size: 25px; font-weight: 700; line-height: 1.12;
  }
  .activities li::before {
    content: ""; position: absolute; left: 2px; top: 9px;
    width: 10px; height: 10px; border-radius: 50%; background: var(--red);
  }
  .badge {
    position: absolute; top: 734px; width: 148px; height: 148px; border-radius: 50%;
    background: var(--white); border: 4px solid var(--ring);
    display: flex; align-items: center; justify-content: center;
  }
  .badge-mascot { left: 40px; }
  .badge-school { left: 238px; }
  .mascot-art { width: 112px; height: 112px; border-radius: 50%; background: radial-gradient(circle, var(--mascot), var(--navy)); }
  .school-name { color: var(--navy); font-size: 24px; font-weight: 800; }
  .contact { position: absolute; left: 36px; color: var(--navy); }
  .contact-email { top: 906px; }
  .contact-text { top: 976px; }
  .contact .icon { position: absolute; left: 0; top: 2px; width: 48px; height: 48px; }
  .contact .body { margin-left: 60px; }
  .contact h3 { margin: 0; font-size: 24px; font-weight: 800; line-height: 1.1; }
  .contact p { margin: 2px 0 0; font-size: 17px; font-weight: 700; line-height: 1.25; white-space: nowrap; }
  .contact .number { font-size: 23px; font-weight: 800; }
</style>
</head>
<body>
  <main class="sign">
    <svg class="sign-footer-bg" viewBox="0 0 440 1100" aria-hidden="true">
      <polygon points="0,782 440,862 440,1100 0,1100" fill="#ffffff"/>
      <rect x="20" y="1068" width="400" height="32" fill="#262a69"/>
    </svg>

    <h1 class="title"><span class="name">LARKFIELD</span><span class="org">PTA</span></h1>
    <div class="rule"></div>

    <h2 class="question">What do<br>we <span class="accent">do</span>?</h2>

    <ul class="activities">
      <li>Help at school events</li>
      <li>Support our school and students</li>
      <li>Organize fundraising events</li>
      <li>Have fun together!</li>
    </ul>

    <div class="badge badge-mascot">
      <div class="mascot-art" role="img" aria-label="School mascot illustration in graduation cap and gown"></div>
    </div>
    <div class="badge badge-school">
      <span class="school-name">Larkfield</span>
    </div>

    <section class="contact contact-email">
      <svg class="icon" viewBox="0 0 48 48" aria-hidden="true">
        <circle cx="24" cy="24" r="24" fill="#262a69"/>
        <text x="24" y="33" text-anchor="middle" font-family="Archivo, Arial, sans-serif" font-weight="900" font-size="28" fill="#ffffff">?</text>
      </svg>
      <div class="body">
        <h3>Questions?</h3>
        <p>Email PTALarkfield@quellmail.com</p>
      </div>
    </section>

    <section class="contact contact-text">
      <svg class="icon" viewBox="0 0 48 48" aria-hidden="true">
        <circle cx="24" cy="24" r="24" fill="#262a69"/>
        <rect x="16" y="12" width="16" height="24" rx="2.5" fill="none" stroke="#ffffff" stroke-width="2.5"/>
        <line x1="20" y1="19" x2="28" y2="19" stroke="#ffffff" stroke-width="2"/>
        <line x1="20" y1="24" x2="28" y2="24" stroke="#ffffff" stroke-width="2"/>
        <line x1="20" y1="29" x2="26" y2="29" stroke="#ffffff" stroke-width="2"/>
      </svg>
      <div class="body">
        <h3>Get Text Updates</h3>
        <p>Text @larkfieldpta to the number</p>
        <p class="number">47326</p>
      </div>
    </section>
  </main>
</body>
</html>
```